Motor Insurance Quotation - New Quote format / New Template

We are a 40 year old insurance company called 'Velmor Insurance Agency L.L.C' in Dubai, UAE (Our logo / color design can and details can be found on www.velmorgulf-example.com).

Velmor provides all kinds of insurance solutions for its clients...currently is this modern fast paced world of ever changing technology and increasing competition we need to be ahead of our competitors...

In order to do so, we are in need to re-design our motor insurance quotation format / template and require it to be more attractive, modern and professional.
Since it is a text heavy format, we need it to look aesthetically appealing to our clients.

We would like to see designs that use our color code (as our website / sample quote currently used is attached)..these designs are required in pdf illustrator formats....i have also attached quotation formats used in the existing market. the template and the samples are only for reference and the templates are not to be followed.

Target Market(s)

UAE

Industry/Entity Type

Insurance

Font styles to use
Other font styles liked:
• arial

Requirements
Must have
• Aesthetic Design, Insurance details and covers provided in our quote, Velmor logo, color code (details can be found on our website)
Nice to have
• 1 page (short quote) and 2 page (detailed quote) designs to shared...

```html
<!DOCTYPE html>
<html lang="en">
<head>
<meta charset="utf-8">
<title>Velmor Motor Insurance Renewal Quotation</title>
<link href="https://fonts.googleapis.com/css2?family=Arimo:wght@400;700&family=Open+Sans:wght@600&display=swap" rel="stylesheet">
<style>
  :root {
    --navy: #363c79;
    --panel: #e7e7e9;
    --ink: #2b2b2b;
    --white: #ffffff;
    --pill: #dcdcdc;
  }
  * { margin: 0; padding: 0; box-sizing: border-box; }
  html, body { width: 849px; height: 1200px; overflow: hidden; background: var(--white); }
  .quote {
    position: relative; width: 849px; height: 1200px; overflow: hidden;
    font-family: "Arimo", Arial, sans-serif; color: var(--ink);
    border-left: 1px solid var(--navy); border-right: 1px solid var(--navy);
  }
  .top-band { position: absolute; left: 0; top: 0; width: 849px; height: 79px; background: var(--navy); }
  .brand-box {
    position: absolute; left: 311px; top: 38px; width: 227px; height: 41px; background: var(--white);
    display: flex; align-items: center; justify-content: center;
  }
  .brand-name { font-family: "Arimo", Arial, sans-serif; font-size: 36px; font-weight: 400; color: var(--navy); letter-spacing: 1px; line-height: 1; }
  .title-bar {
    position: absolute; left: 0; top: 79px; width: 849px; height: 43px;
    border-bottom: 3px solid var(--navy);
    font-family: "Open Sans", Arial, sans-serif; font-weight: 600; font-size: 16.5px; color: #222;
    text-align: center; line-height: 46px;
  }
  .letter { position: absolute; left: 30px; font-size: 16px; line-height: 19px; }
  .salutation { top: 142px; }
  .intro { top: 197px; width: 760px; }
  .section-title { position: absolute; left: 32px; font-size: 16px; font-weight: 700; }
  .section-panel {
    position: absolute; left: 30px; width: 775px; background: var(--panel);
    border-top: 4px solid var(--navy); font-size: 16px; line-height: 19px;
  }
  .cell { position: absolute; white-space: nowrap; }
  .footer { position: absolute; left: 0; top: 1121px; width: 849px; height: 79px; background: var(--navy); }
  .phone-icon { position: absolute; left: 137px; top: 1144px; }
  .phone-number { position: absolute; left: 187px; top: 1149px; font-size: 21px; font-weight: 700; color: var(--white); }
  .email-pill {
    position: absolute; left: 395px; top: 1145px; width: 114px; height: 27px; border-radius: 14px;
    background: var(--pill); color: #555; font-weight: 700; font-size: 16px; text-align: center; line-height: 27px;
  }
  .email-address { position: absolute; left: 520px; top: 1147px; font-size: 21px; font-weight: 700; color: var(--white); }
</style>
</head>
<body>
<div class="quote">
  <div class="top-band"></div>
  <div class="brand-box"><span class="brand-name">VELMOR</span></div>
  <div class="title-bar">MOTOR COMPREHENSIVE, FIRE, THEFT &amp; THIRD PARTY LIABILITY</div>

  <p class="letter salutation">Dear SAMIR HADDAD ALKARIMI NOORANI,</p>
  <p class="letter intro">We are writing to remind you that your motor insurance policy is due for renewal on 22 Dec 2015.<br>Based on the information<br>that we have from your previous policy, the cost of renewing your motor insurance with us is<br>AED2,373<br>If any of the information in this renewal quotation is incorrect or any of your details have changed,<br>please call us on 800 7310<br>or email us at renewals@velmorgulf-example.com so we can amend your renewal quotation accordingly.</p>

  <h2 class="section-title" style="top:349px">Your Details</h2>
  <section class="section-panel" style="top:376px;height:159px">
    <div class="cell" style="left:22px;top:18px">Insured:<br><br>Mobile:<br>Email:<br>Address:</div>
    <div class="cell" style="left:149px;top:18px">SAMIR HADDAD ALKARIMI<br>NOORANI<br>971500000147<br>s.alkarimi@example-mail.com<br>48210<br>Dubai UAE</div>
    <div class="cell" style="left:426px;top:75px">P.O. Box: 48210</div>
  </section>

  <h2 class="section-title" style="top:543px">Insurance Details</h2>
  <section class="section-panel" style="top:570px;height:158px">
    <div class="cell" style="left:22px;top:18px">Period of insurance:<br>Quotation number:<br>Date of issue:<br>Insurance type:</div>
    <div class="cell" style="left:305px;top:18px">23 Dec 2015 - 22 Dec 2016 inclusive<br>AE-MOPL-Q10387248<br>1 Nov 2015<br>Elite</div>
  </section>

  <h2 class="section-title" style="top:736px">Miscellaneous</h2>
  <section class="section-panel" style="top:763px;height:158px">
    <div class="cell" style="left:22px;top:18px">Hire car with pickup and<br>delivery<br>Hire car lump sum<br>No claims</div>
    <div class="cell" style="left:426px;top:37px">10 Days<br><br>discount protection</div>
  </section>

  <h2 class="section-title" style="top:929px">Miscellaneous</h2>
  <section class="section-panel" style="top:956px;height:158px">
    <div class="cell" style="left:22px;top:18px">Hire car with pickup and<br>delivery<br>Hire car lump sum<br>No claims</div>
    <div class="cell" style="left:426px;top:37px">10 Days<br><br>discount protection</div>
  </section>

  <footer class="footer"></footer>
  <svg class="phone-icon" width="34" height="34" viewBox="0 0 34 34" aria-hidden="true">
    <circle cx="17" cy="17" r="16" fill="#d9d9d9"/>
    <path d="M12 9c1 0 2 3 2.5 4.5.3 1-1.5 2-1.2 2.8.8 1.8 2.2 3.3 4 4.2.8.3 1.8-1.5 2.8-1.2 1.5.5 4.4 1.5 4.4 2.5 0 1.5-1.8 3.2-3.5 3.2C15 25 9 19 9 12.5 9 10.8 10.5 9 12 9z" fill="#8a8a8a"/>
  </svg>
  <div class="phone-number">+971 4 000 4477</div>
  <div class="email-pill">EMAIL US</div>
  <div class="email-address">care@velmorgulf-example.com</div>
</div>
</body>
</html>
```